Two Bodyguards

Cover for a book in French language:
- Author: Mathieu Ferrand-Lacoste
- Title: Cold suspects rarely ever smile back
- Publisher (at the bottom of the page): Editions Vernaille
Key Words:
- a rich man died recently, it looks like a murder. He has been found in his luxury apartment.
- Two Body Guards: one is elegant, the other a bit fat.
- two pretty women.
- Inheritance (wealth)
Size of the cover: 14 x 20.5 cm (+ bleed area)
Please note that the title should remain in English: "Suspects rarely ever smile back".
By the way the title doesn't mean anything. It's just a joke.
Thrillers' reader

```html
<!DOCTYPE html>
<html lang="en">
<head>
<meta charset="utf-8">
<title>Suspects rarely ever smile back — book cover</title>
<link rel="stylesheet" href="https://fonts.googleapis.com/css2?family=Bebas+Neue&family=Open+Sans:wght@400&display=swap">
<style>
  :root {
    --ink: #070707;
    --spine-rule: #8a8a8a;
    --gold-deep: #5a3f12;
    --gold: #c8961f;
    --gold-light: #dcae34;
    --blood: #851316;
    --blood-dark: #5e0c0e;
    --author-red: #7a1410;
    --spine-gold: #d9a42a;
    --paper-white: #f4f1ec;
  }
  * { margin: 0; padding: 0; box-sizing: border-box; }
  html, body { width: 1200px; height: 800px; overflow: hidden; background: var(--ink); }
  .cover { position: relative; width: 1200px; height: 800px; }

  /* Back cover */
  .back {
    position: absolute; left: 0; top: 0; width: 557px; height: 800px;
    background: linear-gradient(180deg, #2a1e12 0%, #140e08 22%, var(--ink) 48%);
  }
  .back-copy {
    position: absolute; left: 74px; top: 98px; width: 404px;
    font-family: "Open Sans", sans-serif; font-size: 13.6px; line-height: 18.4px;
    color: var(--paper-white); text-align: justify;
  }
  .back-copy p + p { margin-top: 18.4px; }

  /* Spine */
  .spine {
    position: absolute; left: 557px; top: 0; width: 83px; height: 800px;
    background: var(--ink); border-left: 1px solid var(--spine-rule);
  }
  .spine-text {
    position: absolute; inset: 0;
    writing-mode: vertical-rl; transform: rotate(180deg);
    display: flex; justify-content: space-between; align-items: center;
    padding: 46px 0 44px;
    font-family: "Bebas Neue", sans-serif; font-size: 31px; line-height: 1;
  }
  .spine-author { color: var(--spine-gold); }
  .spine-title { color: var(--paper-white); }

  /* Front cover */
  .front {
    position: absolute; left: 640px; top: 0; width: 560px; height: 800px; overflow: hidden;
    background: linear-gradient(180deg, var(--gold-deep) 0%, #8a6418 14%, var(--gold) 30%, var(--gold-light) 60%, var(--gold) 100%);
  }
  .title-band {
    position: absolute; display: flex; align-items: center; justify-content: center;
    background: linear-gradient(135deg, var(--blood) 0%, var(--blood-dark) 50%, var(--blood) 100%);
    font-family: "Bebas Neue", sans-serif; color: var(--paper-white); line-height: 1;
  }
  .title-line-1 { left: 0; top: 75px; width: 487px; height: 78px; font-size: 92px; padding-top: 6px; }
  .title-line-2 { left: 61px; top: 142px; width: 499px; height: 66px; font-size: 74px; padding-top: 6px; }
  .title-line-3 { left: 121px; top: 203px; width: 304px; height: 71px; font-size: 74px; padding-top: 6px; }

  .jackets {
    position: absolute; left: 12px; top: 296px; width: 526px; height: 390px;
    border-radius: 40px 40px 60px 60px;
    background: radial-gradient(ellipse at 50% 45%, #2e2e2e 0%, #181818 60%, rgba(20,20,20,0) 100%);
  }
  .front-author {
    position: absolute; left: 0; top: 708px; width: 560px; text-align: center;
    font-family: "Bebas Neue", sans-serif; font-size: 54px; line-height: 1;
    color: var(--author-red); padding-left: 40px;
  }
</style>
</head>
<body>
<div class="cover">
  <section class="back" role="img" aria-label="Dark background with faint brown paisley fabric pattern fading to black">
    <div class="back-copy">
      <p>Lorem ipsum dolor sit amet, consectetur adipiscing elit. Etiam eleifend nec arcu eu dapibus. Aenean ipsum leo, bibendum sed auctor vitae, varius id neque. Pellentesque pharetra ante cursus nibh molestie vestibulum. Integer congue euismod faucibus. Pellentesque ut suscipit ex, ac iaculis velit. Sed lorem ante, malesuada eu rhoncus sed, molestie vel risus. Donec ac dapibus velit. Sed interdum varius gravida. Sed vehicula, elit ut tempor aliquet, felis velit posuere massa, blandit mattis arcu nisl sodales sem.</p>
      <p>Vivamus bibendum fringilla placerat. Aenean efficitur nulla nec bibendum aliquam. Suspendisse mauris urna, dictum non diam nec, porttitor porttitor nisi. Nulla molestie, arcu ut pellentesque ultrices, lectus nisi varius leo, facilisis lobortis lorem nibh et augue. Morbi ut risus vitae purus ornare interdum et nec diam. Donec sollicitudin, dolor quis feugiat dignissim, tortor eros fermentum est, sed facilisis justo purus sed mi.</p>
      <p>Donec interdum laoreet ipsum, et congue ipsum condimentum fringilla. Praesent commodo imperdiet lobortis. Mauris in tempor justo. Nam egestas sem vel bibendum aliquet. Orci varius natoque penatibus et magnis dis parturient montes, nascetur ridiculus mus. Etiam nisl tortor, fringilla eu dapibus vel, ttis.</p>
    </div>
  </section>

  <section class="spine">
    <div class="spine-text">
      <span class="spine-author">MATHIEU FERRAND-LACOSTE</span>
      <span class="spine-title">SUSPECTS RARELY EVER SMILE BACK</span>
    </div>
  </section>

  <section class="front" role="img" aria-label="Gold textured background with brown paisley fabric along the top">
    <h1>
      <span class="title-band title-line-1">SUSPECTS</span>
      <span class="title-band title-line-2">RARELY EVER</span>
      <span class="title-band title-line-3">SMILE BACK</span>
    </h1>
    <div class="jackets" role="img" aria-label="Two empty black suit jackets standing side by side, one slim, one broader"></div>
    <p class="front-author">MATHIEU FERRAND-LACOSTE</p>
  </section>
</div>
</body>
</html>
```